BRSP Business Card Design Project

We are a Wedding Film company in Charleston, SC In need of a unique business card. Our website is www.brightspiralreels.example. Check us out to get an idea of who we are and what we do. The design should be upscale but not pretentious. Modern but not cheesy. I will most likely have our cards printed by Zib on the Opal design. I'm also liking the raised designs for our logo. The Wedding Films in our logo on our site is blue so feel free to manipulate our logo for your designs as well.

Industry/Entity Type

Business

Requirements
Must have
• This is the info I want on the card:

Derek Hollisbury
Storyteller

Brightspiral Wedding Reels
www.brightspiralreels.example

555.208.4417
derek@brightspiralreels.example

```html
<!DOCTYPE html>
<html lang="en">
<head>
<meta charset="utf-8">
<title>Brightspiral Wedding Reels — Business Card</title>
<link rel="stylesheet" href="https://fonts.googleapis.com/css2?family=Josefin+Sans:wght@300;400;600&family=Pinyon+Script&display=swap">
<style>
  :root {
    --bg: #f2f0ec;
    --card: #ffffff;
    --bronze: #7a5c12;
    --gold-ink: #8a6a1f;
    --gold-soft: #c9b27a;
    --on-bronze: #ffffff;
  }
  * { box-sizing: border-box; margin: 0; padding: 0; }
  html, body { width: 1200px; height: 1200px; overflow: hidden; }
  body {
    background: var(--bg);
    display: flex;
    align-items: center;
    justify-content: center;
    font-family: "Josefin Sans", "Century Gothic", sans-serif;
  }
  .card {
    position: relative;
    width: 560px;
    height: 980px;
    background: var(--card);
    box-shadow: 0 10px 40px rgba(0,0,0,0.12);
    overflow: hidden;
  }
  .scallop-edge { position: absolute; left: 0; width: 560px; display: block; }
  .scallop-edge--top { top: 0; height: 60px; }
  .scallop-edge--bottom { bottom: 0; height: 300px; }

  .brand {
    position: absolute;
    top: 110px; left: 0; right: 0;
    display: flex; flex-direction: column; align-items: center;
  }
  .brand__mark {
    width: 96px; height: 96px; border-radius: 50%;
    background: var(--gold-soft);
    margin-bottom: 18px;
  }
  .brand__name {
    font-weight: 300;
    font-size: 62px;
    letter-spacing: 1px;
    color: var(--gold-ink);
  }

  .person {
    position: absolute;
    top: 360px; left: 0; right: 0;
    text-align: center;
  }
  .person__name {
    font-family: "Pinyon Script", cursive;
    font-size: 58px;
    color: var(--gold-ink);
    line-height: 1.1;
  }
  .person__title {
    margin-top: 14px;
    font-size: 30px;
    color: var(--gold-ink);
  }

  .ornament {
    position: absolute;
    top: 520px; left: 170px;
    width: 220px; height: 170px;
    background: radial-gradient(ellipse at center, #e7dcc0 0%, #f6f1e4 60%, rgba(255,255,255,0) 100%);
  }

  .contact {
    position: absolute;
    left: 0; right: 0; bottom: 34px;
    text-align: center;
    color: var(--on-bronze);
    font-weight: 600;
    font-size: 25px;
    line-height: 1.6;
    letter-spacing: 0.3px;
  }
  .contact__phone { letter-spacing: 2px; }
</style>
</head>
<body>
  <main class="card">
    <svg class="scallop-edge scallop-edge--top" viewBox="0 0 560 60" aria-hidden="true">
      <defs>
        <pattern id="scallopDown" width="28" height="60" patternUnits="userSpaceOnUse">
          <rect x="0" y="0" width="28" height="30" fill="#7a5c12"/>
          <circle cx="14" cy="30" r="14" fill="#7a5c12"/>
        </pattern>
      </defs>
      <rect width="560" height="60" fill="url(#scallopDown)"/>
    </svg>

    <div class="brand">
      <div class="brand__mark" role="img" aria-label="Tree emblem of the company logo"></div>
      <div class="brand__name">Brightspiral</div>
    </div>

    <section class="person">
      <h1 class="person__name">Derek Hollisbury</h1>
      <p class="person__title">Storyteller</p>
    </section>

    <div class="ornament" role="img" aria-label="Decorative gold swirl ornament"></div>

    <svg class="scallop-edge scallop-edge--bottom" viewBox="0 0 560 300" aria-hidden="true">
      <defs>
        <pattern id="scallopUp" width="28" height="300" patternUnits="userSpaceOnUse">
          <rect x="0" y="14" width="28" height="286" fill="#7a5c12"/>
          <circle cx="14" cy="14" r="14" fill="#7a5c12"/>
        </pattern>
      </defs>
      <rect width="560" height="300" fill="url(#scallopUp)"/>
    </svg>

    <address class="contact">
      <div class="contact__company">Brightspiral Wedding Reels</div>
      <div class="contact__web">www.brightspiralreels.example</div>
      <div class="contact__phone">555.208.4417</div>
      <div class="contact__email">derek@brightspiralreels.example</div>
    </address>
  </main>
</body>
</html>
```